Veltiwell- Comprehensive quality healthcare delivered at your door.

I am looking for brochures to help promote my business. My business name is Veltiwel (see attachment and logo). This is a new health delivery system designed to provide high quality care to elderly in their communities or at home.

See attachements. The logo is already designed.

As far as services provided (see attachment)

Target Market(s)

Elderly patients

Industry/Entity Type

Business

Font styles to use
Serif

Colors

Designer to choose colors to be used in the design.

```html
<!DOCTYPE html>
<html lang="en">
<head>
<meta charset="utf-8">
<title>Veltiwel Brochure Cover</title>
<link rel="stylesheet" href="https://fonts.googleapis.com/css2?family=Cinzel:wght@500&family=Nunito+Sans:wght@300;400&display=swap">
<style>
  :root {
    --backdrop: #fdf0cf;
    --paper: #ffffff;
    --band-1: #dfe8bc;
    --band-2: #c1d08f;
    --band-3: #a0b55e;
    --band-4: #7a9a3c;
    --ink-dark: #2e3b1c;
    --ink-band: #4d5e2a;
    --ink-light: #ffffff;
    --badge: #2e3b1c;
  }
  html, body {
    margin: 0;
    padding: 0;
    width: 900px;
    height: 1200px;
    overflow: hidden;
    background: var(--backdrop);
  }
  .canvas {
    position: relative;
    width: 900px;
    height: 1200px;
  }
  .brochure-cover {
    position: absolute;
    left: 252px;
    top: 69px;
    width: 410px;
    height: 944px;
    background: var(--paper);
    overflow: hidden;
    font-family: "Nunito Sans", sans-serif;
    box-shadow: 3px 4px 6px rgba(120, 100, 60, 0.25);
  }
  .service-band {
    position: absolute;
    left: 0;
    width: 100%;
    height: 51px;
    display: flex;
    align-items: center;
    justify-content: center;
    font-size: 21px;
    font-weight: 300;
    letter-spacing: 0.4px;
    line-height: 1;
  }
  .service-band--chronic { top: 28px;  background: var(--band-1); color: var(--ink-band); }
  .service-band--physical { top: 98px; background: var(--band-2); color: var(--ink-band); }
  .service-band--rehab { top: 169px;   background: var(--band-3); color: var(--ink-light); }
  .service-band--meds { top: 239px;    background: var(--band-4); color: var(--ink-light); }
  .hero-photo {
    position: absolute;
    left: 0;
    top: 308px;
    width: 100%;
    height: 321px;
    background:
      radial-gradient(ellipse at 50% 20%, #e9f1d6 0%, rgba(233,241,214,0) 60%),
      linear-gradient(180deg, #9fbf6a 0%, #b9c9a0 45%, #8f8a9c 80%, #a3b98a 100%);
  }
  .accent-rule {
    position: absolute;
    left: 0;
    top: 629px;
    width: 100%;
    height: 8px;
    background: var(--band-4);
  }
  .brand-badge {
    position: absolute;
    left: 134px;
    top: 594px;
    width: 142px;
    height: 142px;
    border-radius: 50%;
    background: var(--badge);
  }
  .brand-name {
    position: absolute;
    left: 0;
    top: 749px;
    width: 100%;
    text-align: center;
    font-family: "Cinzel", serif;
    font-size: 40px;
    font-weight: 500;
    line-height: 1;
    letter-spacing: 0;
    color: var(--ink-dark);
    margin: 0;
  }
  .tagline {
    position: absolute;
    left: 0;
    top: 830px;
    width: 100%;
    text-align: center;
    font-size: 15px;
    font-weight: 400;
    line-height: 1.2;
    color: var(--ink-dark);
    margin: 0;
  }
</style>
</head>
<body>
  <div class="canvas">
    <section class="brochure-cover">
      <div class="service-band service-band--chronic">Chronic Care Management</div>
      <div class="service-band service-band--physical">Physical Therapy</div>
      <div class="service-band service-band--rehab">Rehabilitation</div>
      <div class="service-band service-band--meds">Medications Management</div>
      <div class="hero-photo" role="img" aria-label="Photo of five smiling older adults in a park stacking their hands together"></div>
      <div class="accent-rule"></div>
      <div class="brand-badge"></div>
      <h1 class="brand-name">VELTIWEL</h1>
      <p class="tagline">Home and Community Based Services for Adults</p>
    </section>
  </div>
</body>
</html>
```